Website design for a steel buildings

We need a new look for our site www.brindlemoorgroupltd.co.uk, we have listed lots of inspirational images although we are looking for a bespoke site that looks nothing like a theme. We have an in-house development team that will build the website and a UX and design team that will proof all designs.
Colours and layout are down to your imagination and with this brand, we are targeting a commercial market. We require the following pages in both mobile and desktop:
Home
Industrial Buildings
Contact Us

The logo will be supplied by our art team.

Target Market(s)

Commercial

Industry/Entity Type

Construction

Number of Pages Required

3 page

Font styles to use
Sans Serif
Other font styles liked:
• Geomanist

Colors

Designer to choose colors to be used in the design.

Requirements
Must have
• Somthing differant to the original site, new content will be supplied after the design.
• Designs for both desktop and mobile.
• Designs supplied as a PSD, All vector images need the originl AI file
• Images cut up and optimised before file hand over
Nice to have
• Animation
Should not have
• Slider as the hero image

```html
<!DOCTYPE html>
<html lang="en">
<head>
<meta charset="utf-8">
<title>Brindlemoor Group</title>
<link href="https://fonts.googleapis.com/css2?family=Roboto:wght@300;400;500;700&display=swap" rel="stylesheet">
<style>
:root{
  --orange:#e8872a;
  --navy:#1c3a5e;
  --navy-dark:#132b47;
  --ink:#2b2b2b;
  --text:#555;
  --muted:#999;
  --line:#e5e5e5;
  --grey-bg:#f3f3f3;
  --footer:#2a2c30;
  --footer-dark:#1f2124;
  --footer-box:#34363b;
}
*{box-sizing:border-box;margin:0;padding:0}
html,body{width:1200px;height:4276px;overflow:hidden}
body{font-family:"Roboto",Arial,sans-serif;color:var(--text);background:#fff;position:relative}
section,header,footer,.bottom-bar{position:relative;width:1200px}
.wrap{position:absolute;left:60px;width:1080px}

/* header */
.site-header{height:114px}
.brand{position:absolute;left:60px;top:30px;display:flex;align-items:center;gap:14px}
.brand-mark{width:40px;height:40px;background:var(--orange)}
.brand-name{font-size:32px;font-weight:700;color:var(--orange);letter-spacing:.5px}
.phone-tab{position:absolute;right:80px;top:0;width:190px;height:40px;background:var(--orange);color:#fff;font-size:18px;font-weight:500;display:flex;align-items:center;justify-content:center;gap:8px;clip-path:polygon(0 0,100% 0,92% 100%,8% 100%)}
.main-nav{position:absolute;right:60px;top:72px;display:flex;gap:34px;font-size:14px;font-weight:500;color:var(--ink)}
.main-nav .active{border-bottom:2px solid var(--ink);padding-bottom:4px}

/* hero */
.hero{height:479px;background:linear-gradient(180deg,#3d3f42 0%,#6b6a66 35%,#a79c8c 60%,#4a4744 100%)}
.hero-title-box{position:absolute;left:310px;top:170px;width:650px;background:rgba(210,210,210,.55);padding:14px 0 10px;text-align:center}
.hero-title{font-size:40px;font-weight:700;color:var(--orange);letter-spacing:1px}
.hero-sub{margin:6px 18px 0;background:rgba(230,230,230,.75);font-size:23px;font-weight:500;color:#1a1a1a;padding:6px 0}

/* welcome */
.welcome{height:262px}
.welcome-head{position:absolute;left:60px;top:70px;width:250px;text-align:right;font-size:36px;font-weight:300;color:var(--ink);line-height:1.1}
.welcome-head span{color:var(--orange)}
.welcome-rule{position:absolute;left:328px;top:66px;width:2px;height:100px;background:var(--orange)}
.welcome-text{position:absolute;left:345px;top:68px;width:795px;font-size:15px;line-height:1.75;color:var(--text)}

/* services */
.services{height:698px}
.service{position:absolute;top:0;width:340px}
.service h3{font-size:22px;font-weight:400;color:var(--ink)}
.service .tag{font-size:13px;color:var(--muted);margin-top:6px;padding-bottom:6px;border-bottom:2px solid var(--orange);display:inline-block}
.service .photo{margin-top:40px;height:240px}
.mini{position:absolute;top:485px;width:340px;height:112px;display:flex;border:1px solid var(--line)}
.mini .thumb{width:110px;height:110px;flex:none}
.mini .body{padding:14px 0 0 18px}
.mini h4{font-size:17px;font-weight:400;color:var(--ink)}
.mini .sub{font-size:12px;color:var(--muted);margin-top:4px}
.mini .more{font-size:12px;color:var(--orange);margin-top:10px}

/* values band */
.values{height:385px;background:var(--navy)}
.value{position:absolute;top:0;height:385px;text-align:center;color:#fff}
.value.first{background:var(--navy-dark)}
.value svg{margin-top:80px}
.value h3{font-size:21px;font-weight:500;margin-top:30px}
.value p{font-size:14px;color:var(--orange);margin:10px auto 0;width:240px;line-height:1.4}
.value-more{position:absolute;left:0;right:0;bottom:0;height:42px;background:var(--orange);color:#fff;font-size:14px;line-height:42px;clip-path:polygon(6% 0,94% 0,100% 100%,0 100%)}

/* about */
.about{height:584px}
.section-title{font-size:30px;font-weight:400;color:var(--ink)}
.title-rule{width:250px;height:1px;background:var(--line);margin-top:10px;position:relative}
.title-rule::before{content:"";position:absolute;left:0;top:-1px;width:60px;height:3px;background:var(--orange)}
.about-photo{position:absolute;left:60px;top:170px;width:250px;height:335px;background:linear-gradient(160deg,#d9dee3,#7f8c98 60%,#2c3540)}
.about-text{position:absolute;left:340px;top:165px;width:390px;font-size:15px;line-height:1.65}
.about-text h4{font-size:18px;font-weight:400;color:var(--orange);margin:14px 0 6px}
.btn{display:inline-block;background:var(--orange);color:#fff;font-size:14px;font-weight:500;text-align:center}
.about-text .btn{margin-top:26px;width:130px;height:44px;line-height:44px}
.quote-box{position:absolute;left:810px;top:80px;width:330px;height:455px;border:1px solid var(--line);padding:30px 22px}
.quote-box h3{font-size:28px;font-weight:300;color:var(--ink);text-align:center}
.quote-box .rule{width:120px;height:2px;background:var(--orange);margin:10px auto 34px}
.field{height:46px;border-bottom:1px solid var(--line);font-size:12px;color:var(--muted);padding-top:16px;margin-bottom:26px;display:flex;justify-content:space-between}
.quote-box .btn{width:100%;height:50px;line-height:50px;margin-top:6px}

/* testimonials */
.testimonials{height:498px;background:var(--grey-bg)}
.more-reviews{position:absolute;right:60px;top:62px;width:140px;height:40px;border:1px solid var(--line);background:#fff;font-size:13px;color:var(--ink);text-align:center;line-height:40px}
.review{position:absolute;top:180px;width:528px;height:245px;background:#fff;padding:22px 28px}
.review .mark{font-size:60px;line-height:40px;color:var(--orange);font-weight:700}
.review p{font-size:14px;line-height:1.65;margin-top:6px}
.reviewer{position:absolute;left:28px;bottom:28px;display:flex;align-items:center;gap:22px;font-size:20px;color:var(--ink)}
.avatar{width:62px;height:62px;border-radius:50%;background:#c9ccd0}

/* news */
.news{height:713px}
.post{position:absolute;top:170px;width:340px;height:445px;border:1px solid var(--line)}
.post .photo{height:195px}
.post .date{position:absolute;left:30px;top:180px;background:var(--orange);color:#fff;font-size:13px;padding:6px 14px}
.post .body{padding:22px 22px 0}
.post .by{font-size:14px;color:var(--muted);margin-top:18px}
.post p{font-size:14px;line-height:1.65;margin-top:12px}
.post .cont{font-size:12px;font-weight:700;color:var(--ink);margin-top:22px;letter-spacing:.3px}

/* footer */
.site-footer{height:479px;background:var(--footer);color:#aaa}
.info-bar{position:absolute;left:60px;top:0;width:1080px;height:80px;background:#222428;display:flex;align-items:center;font-size:14px}
.info-bar div{flex:1;display:flex;align-items:center;gap:10px;padding-left:30px}
.info-bar b{color:#fff;font-weight:500}
.fcol{position:absolute;top:140px}
.fcol h4{font-size:16px;font-weight:500;color:#fff;margin-bottom:22px}
.fcol p,.fcol li{font-size:14px;line-height:1.7}
.fcol ul{list-style:none}
.fcol li{margin-bottom:9px}
.fcol li::before{content:"›";margin-right:10px;color:#aaa}
.socials{display:flex;gap:12px;margin-top:26px}
.socials span{width:34px;height:34px;border-radius:50%;border:1px solid #555}
.recent .item{display:flex;gap:12px;margin-bottom:18px}
.recent .t{font-size:14px;color:#ddd}
.recent .d{font-size:12px;color:#999;margin-top:4px}
.newsletter{position:absolute;left:890px;top:140px;width:250px;height:300px;background:var(--footer-box);padding:22px}
.newsletter h4{font-size:16px;font-weight:500;color:#fff;margin-bottom:16px}
.newsletter p{font-size:13px;line-height:1.6}
.email{margin-top:22px;height:42px;border:1px solid #555;font-size:12px;padding:13px 12px;color:#888;display:flex;justify-content:space-between}
.newsletter .btn{width:100%;height:46px;line-height:46px;margin-top:16px;font-size:16px}
.bottom-bar{height:64px;background:var(--footer-dark);font-size:14px;color:#aaa}
.bottom-bar .l{position:absolute;left:60px;top:23px}
.bottom-bar .l b{color:#fff;font-weight:500}
.bottom-bar .r{position:absolute;right:60px;top:23px}
</style>
</head>
<body>

<header class="site-header">
  <div class="brand"><span class="brand-mark"></span><span class="brand-name">BRINDLEMOOR GROUP</span></div>
  <div class="phone-tab">
    <svg width="16" height="16" viewBox="0 0 24 24"><path fill="#fff" d="M6.6 10.8a15.1 15.1 0 0 0 6.6 6.6l2.2-2.2c.3-.3.7-.4 1-.2 1.1.4 2.3.6 3.6.6.6 0 1 .4 1 1V20c0 .6-.4 1-1 1A17 17 0 0 1 3 4c0-.6.4-1 1-1h3.5c.6 0 1 .4 1 1 0 1.3.2 2.5.6 3.6.1.3 0 .7-.2 1z"/></svg>
    0345 610 4478
  </div>
  <nav class="main-nav"><span class="active">ABOUT US</span><span>FREE QUOTATION</span><span>CONTACT US</span></nav>
</header>

<section class="hero" role="img" aria-label="Close-up photograph of stacked steel reinforcing bars">
  <div class="hero-title-box">
    <div class="hero-title">BRINDLEMOOR GROUP</div>
    <div class="hero-sub">We are a competitive &amp; reliable steel building specialist</div>
  </div>
</section>

<section class="welcome">
  <h2 class="welcome-head">Welcome<br>to our <span>industry</span></h2>
  <div class="welcome-rule"></div>
  <p class="welcome-text">We have facility to produce advance work various industrial applications based on specially developed technology. We are also ready to developement by according to users changing needs. Infrastructure related installation projects. General repair &amp; industrial and machinery</p>
</section>

<section class="services">
  <div class="service" style="left:60px"><h3>Agriculture Processing</h3><span class="tag">Technoeconomic Activities</span>
    <div class="photo" role="img" aria-label="Rolled steel coils" style="background:linear-gradient(135deg,#5c7480,#b8c4ca 50%,#6d7f87)"></div></div>
  <div class="service" style="left:430px"><h3>Mechanical Engineering</h3><span class="tag">Manufacturing &amp; Maintenance</span>
    <div class="photo" role="img" aria-label="Sparks flying from a grinder cutting a steel pipe" style="background:linear-gradient(135deg,#2a1a10,#c4561e 50%,#3a2416)"></div></div>
  <div class="service" style="left:800px"><h3>Chemical Research</h3><span class="tag">Pharmaceutical Sectors</span>
    <div class="photo" role="img" aria-label="Ends of stacked steel rods" style="background:linear-gradient(135deg,#8a7f70,#d1c5b2 50%,#6d6458)"></div></div>

  <div class="mini" style="left:60px"><div class="thumb" role="img" aria-label="Oil pump jack at sunset" style="background:linear-gradient(180deg,#c99a62,#4a3a2a)"></div>
    <div class="body"><h4>Petroleum and Gas</h4><div class="sub">Production of Hydrocarbons</div><div class="more">Read More</div></div></div>
  <div class="mini" style="left:430px"><div class="thumb" role="img" aria-label="Engineer working with materials" style="background:linear-gradient(180deg,#6b7580,#2c333a)"></div>
    <div class="body"><h4>Material Engineering</h4><div class="sub">Development of materials</div><div class="more">Read More</div></div></div>
  <div class="mini" style="left:800px"><div class="thumb" role="img" aria-label="Solar panels in sunlight" style="background:linear-gradient(180deg,#e8d27a,#5e6b3a)"></div>
    <div class="body"><h4>Power and Energy</h4><div class="sub">From sunlight into electricity</div><div class="more">Read More</div></div></div>
</section>

<section class="values">
  <div class="value first" style="left:60px;width:340px">
    <svg width="90" height="90" viewBox="0 0 90 90"><polygon points="24,6 66,6 86,45 66,84 24,84 4,45" fill="none" stroke="#fff" stroke-width="2"/><circle cx="45" cy="40" r="11" fill="none" stroke="#fff" stroke-width="2"/><path d="M30 60 Q45 48 60 60" fill="none" stroke="#fff" stroke-width="2"/></svg>
    <h3>Creditable Integrity</h3><p>Value talent cultivation and encourage creative innovation</p>
    <div class="value-more">Read More &gt;&gt;</div>
  </div>
  <div class="value" style="left:400px;width:370px">
    <svg width="90" height="90" viewBox="0 0 90 90"><polygon points="24,6 66,6 86,45 66,84 24,84 4,45" fill="none" stroke="#fff" stroke-width="2"/><rect x="32" y="30" width="26" height="30" rx="3" fill="none" stroke="#fff" stroke-width="2"/><path d="M38 42h14M38 50h14" stroke="#fff" stroke-width="2"/></svg>
    <h3>Effective Team Work</h3><p>Value talent cultivation and encourage creative innovation</p>
  </div>
  <div class="value" style="left:770px;width:370px">
    <svg width="90" height="90" viewBox="0 0 90 90"><polygon points="24,6 66,6 86,45 66,84 24,84 4,45" fill="none" stroke="#fff" stroke-width="2"/><circle cx="45" cy="40" r="12" fill="none" stroke="#fff" stroke-width="2"/><path d="M38 50l-4 14 11-5 11 5-4-14" fill="none" stroke="#fff" stroke-width="2"/></svg>
    <h3>Quality Assurance</h3><p>Value talent cultivation and encourage creative innovation</p>
  </div>
</section>

<section class="about">
  <div class="wrap" style="top:68px;width:680px"><h2 class="section-title">About Our Industry</h2><div class="title-rule"></div></div>
  <div class="about-photo" role="img" aria-label="Two engineers in hard hats reviewing plans"></div>
  <div class="about-text">
    <p>When you give to Our Industry, know your donation is making a difference whether you are supporting our signature Programs or our carefully curated list of gifts that professional.</p>
    <h4>History in Words</h4>
    <p>We partner with over 320 amazing seds projects world-wide, and have given over million in cash &amp; product grants to other groups since 2015 our own dynamic suite.</p>
    <span class="btn">Read More</span>
  </div>
  <div class="quote-box">
    <h3>Reuest for Quote</h3><div class="rule"></div>
    <div class="field">Your Name*</div>
    <div class="field">Your Mail*</div>
    <div class="field">Select Service <span>⌄</span></div>
    <span class="btn">Get A Quote</span>
  </div>
</section>

<section class="testimonials">
  <div class="wrap" style="top:66px;width:600px"><h2 class="section-title">Words From Customers</h2><div class="title-rule"></div></div>
  <div class="more-reviews">More Reviews</div>
  <div class="review" style="left:60px"><div class="mark">“</div>
    <p>We partner with over 320 amazing seds projects worldwide, and have given over million in cash &amp; product grants to other groups since 2015 our own dynamic suite.</p>
    <div class="reviewer"><span class="avatar" role="img" aria-label="Customer portrait"></span>Elena Marsh</div></div>
  <div class="review" style="left:612px"><div class="mark">“</div>
    <p>We partner with over 320 amazing seds projects worldwide, and have given over million in cash &amp; product grants to other groups since 2015 our own dynamic suite.</p>
    <div class="reviewer"><span class="avatar" role="img" aria-label="Customer portrait"></span>Owen Calder</div></div>
</section>

<section class="news">
  <div class="wrap" style="top:86px;width:600px"><h2 class="section-title">Latest News this month</h2><div class="title-rule"></div></div>
  <article class="post" style="left:60px"><div class="photo" role="img" aria-label="Oil pump jack under a blue sky" style="background:linear-gradient(180deg,#7aa3c4,#2d4a63)"></div>
    <span class="date">August 25,2017</span>
    <div class="body"><div class="by">by Ruth Penrose</div><p>We partner with over 320 amazing seds projects worldwide, and have given over million in cash &amp; product grants to other groups since 2015 our own dynamic suite.</p><div class="cont">CONTINUE READING...</div></div></article>
  <article class="post" style="left:430px"><div class="photo" role="img" aria-label="Offshore platform with yellow steel structure" style="background:linear-gradient(180deg,#4f8ad0,#d9b53a)"></div>
    <span class="date">August 25,2017</span>
    <div class="body"><div class="by">by Dale Whitcombe</div><p>We partner with over 320 amazing seds projects worldwide, and have given over million in cash &amp; product grants to other groups since 2015 our own dynamic suite.</p><div class="cont">CONTINUE READING...</div></div></article>
  <article class="post" style="left:800px"><div class="photo" role="img" aria-label="Engineers at an industrial plant" style="background:linear-gradient(180deg,#c9d3dc,#55606b)"></div>
    <span class="date">September 25,2017</span>
    <div class="body"><div class="by">by Ruth Penrose</div><p>We partner with over 320 amazing seds projects worldwide, and have given over million in cash &amp; product grants to other groups since 2015 our own dynamic suite.</p><div class="cont">CONTINUE READING...</div></div></article>
</section>

<footer class="site-footer">
  <div class="info-bar">
    <div><svg width="18" height="18" viewBox="0 0 24 24"><path fill="#e8872a" d="M6.6 10.8a15.1 15.1 0 0 0 6.6 6.6l2.2-2.2c.3-.3.7-.4 1-.2 1.1.4 2.3.6 3.6.6.6 0 1 .4 1 1V20c0 .6-.4 1-1 1A17 17 0 0 1 3 4c0-.6.4-1 1-1h3.5c.6 0 1 .4 1 1 0 1.3.2 2.5.6 3.6.1.3 0 .7-.2 1z"/></svg><span><b>Phone:</b> +0161-555-2190 &amp; 204</span></div>
    <div><svg width="18" height="18" viewBox="0 0 24 24"><path fill="#e8872a" d="M12 2a7 7 0 0 0-7 7c0 5 7 13 7 13s7-8 7-13a7 7 0 0 0-7-7zm0 9.5A2.5 2.5 0 1 1 12 6.5a2.5 2.5 0 0 1 0 5z"/></svg><span><b>Address:</b> 48 Foundry Lane, Ashby Yard, UK</span></div>
    <div><svg width="18" height="18" viewBox="0 0 24 24"><circle cx="12" cy="12" r="9" fill="none" stroke="#e8872a" stroke-width="2"/><path d="M12 7v5l3 3" fill="none" stroke="#e8872a" stroke-width="2"/></svg><span><b>Working Hrs:</b> Mon - Sat: 9am to 18pm</span></div>
  </div>
  <div class="fcol" style="left:60px;width:230px"><h4>ABOUT US</h4>
    <p>Over 24 years experience and knowledge international standards, technologicaly changes our industrial systems, we are dedicated to provides the best solutions to our valued customers there are many variations solutions.</p>
    <div class="socials"><span></span><span></span><span></span><span></span></div></div>
  <div class="fcol" style="left:368px;width:200px"><h4>USEFULL LINKS</h4>
    <ul><li>Agriculture Processing</li><li>Mechanical Engineering</li><li>Chemical Research</li><li>Petroleum and Gas</li><li>Material Engineering</li><li>Power and Energy</li></ul></div>
  <div class="fcol recent" style="left:618px;width:240px"><h4>RECENT POST</h4>
    <div class="item"><span style="color:#e8872a">→</span><div><div class="t">Best factory award of the year</div><div class="d">March 16, 2017</div></div></div>
    <div class="item"><span style="color:#e8872a">→</span><div><div class="t">Our great working environment</div><div class="d">February 27, 2017</div></div></div>
    <div class="item"><span style="color:#e8872a">→</span><div><div class="t">How to find good engineers?</div><div class="d">January 05, 2017</div></div></div></div>
  <div class="newsletter"><h4>NEWSLETTER</h4>
    <p>Subscribe to our nesletter, We don't do mail to spam &amp; your mail id is very confidential.</p>
    <div class="email">Email address <span>✉</span></div>
    <span class="btn">Subscribe us</span></div>
</footer>

<div class="bottom-bar">
  <div class="l"><b>Any Queries:</b> help@brindlemoorworks.com</div>
  <div class="r">Copyrights © 2017 All Rights Reserved. Brindlemoor Group</div>
</div>

</body>
</html>
```